Create a Diagram for our Company! How a VPN Works

Require a simple/easy to understand diagram that shows users how a VPN works & why they would need one.

I just need this in ONE diagram/whole design.

My preferred concept it;

*** OUTSIDE PART OF DIAGRAM: On the outside part of diagram, I would like pictures which represents the below as though they are trying to look/get in. (see attached for examples)
- eyes
- police
- government
- internet provider
- hackers
- companies

*** INSIDE PART OF DIAGRAM: On the inside of the secure VPN tunnel/cloud/pipe, I would like the words or pictures representing the below.
- download
- unlock worldwide internet content
- sports
- streaming

Additionally the diagram needs to show everything inside the secure part is safe from the outside world.

Looking forward to see your work! Let me know if you have questions.

The winning job will be the diagram which shows what a VPN is to someone who has no idea what one is. I encourage you to use your design skills and be innovative.

Target Market(s)

Home Users both technical and non technical

Website visitors and households who do not know what a VPN is, how it works and why they need one.

Industry/Entity Type

Computer Security

Font styles to use
Serif

Requirements
Must have
• Easy to understand
• Modern Icons/Images
Nice to have
• The diagram does not have to be like I described above however must meet the project brief.

```html
<!DOCTYPE html>
<html lang="en">
<head>
<meta charset="utf-8">
<title>How VPN Works</title>
<link href="https://fonts.googleapis.com/css2?family=Bebas+Neue&family=Open+Sans:wght@400;600;700;800&display=swap" rel="stylesheet">
<style>
  :root {
    --sky-top: #fdf1e6;
    --sky-mid: #f7a937;
    --dusk: #5a4a3a;
    --night: #0b0b0b;
    --orange: #f7941d;
    --orange-deep: #e2571f;
    --badge-red: #d7262f;
    --pill-dark: #2b2b2b;
    --pill-mid: #555555;
    --white: #ffffff;
    --dash: #c9b38f;
    --footer: #e4e9ee;
    --ink: #1d1d1d;
    --screen: #2aa59b;
    --figure-top: #4a4a4a;
    --figure-bottom: #1a1a1a;
  }
  * { margin: 0; padding: 0; box-sizing: border-box; }
  html, body { width: 1200px; height: 571px; overflow: hidden; background: var(--night); }
  .canvas {
    position: relative; width: 1200px; height: 571px; overflow: hidden;
    font-family: "Open Sans", Arial, sans-serif;
  }
  .backdrop {
    position: absolute; left: 0; top: 0; width: 1200px; height: 506px;
    background: linear-gradient(180deg, var(--sky-top) 0%, #fbd7a6 14%, var(--sky-mid) 32%, #a87a40 48%, var(--dusk) 58%, #151515 70%, var(--night) 100%);
  }
  .title-pill {
    position: absolute; left: 364px; top: 24px; width: 464px; height: 92px;
    border-radius: 46px;
    background: linear-gradient(180deg, var(--pill-mid) 0%, var(--pill-dark) 100%);
    display: flex; align-items: center; justify-content: center;
    font-family: "Bebas Neue", "Arial Narrow", sans-serif;
    font-size: 74px; line-height: 1; letter-spacing: 1.5px; color: var(--white);
    padding-top: 6px;
  }
  .diagram-lines { position: absolute; left: 0; top: 0; }
  .tag {
    position: absolute; height: 21px; border-radius: 11px;
    background: var(--night); color: var(--white);
    font-size: 12px; display: flex; align-items: center; justify-content: center;
  }
  .tag--internet { height: 28px; border-radius: 14px; font-size: 15px; letter-spacing: .5px; }
  .device {
    position: absolute; width: 194px; height: 112px;
    background: linear-gradient(180deg, #3a3a3a 0%, #3a3a3a 88%, #cfcfcf 88%, #9a9a9a 100%);
    border-radius: 8px 8px 4px 4px;
  }
  .device::after {
    content: ""; position: absolute; left: 12px; top: 8px; width: 170px; height: 86px;
    background: linear-gradient(135deg, #33b3a8 0%, var(--screen) 60%, #23867e 100%);
    border-radius: 2px;
  }
  .figure {
    position: absolute; border-radius: 8px;
    background: linear-gradient(180deg, var(--figure-top) 0%, var(--figure-bottom) 100%);
    opacity: .9;
  }
  .device-label {
    position: absolute; width: 220px; text-align: center; color: var(--white);
  }
  .device-label__title {
    display: block; color: var(--orange); font-weight: 800; font-size: 16px; letter-spacing: .9px;
  }
  .device-label__role { display: block; font-size: 14px; margin-top: 3px; }
  .note {
    position: absolute; color: var(--white); font-size: 13.5px; text-align: center; line-height: 19px;
  }
  .brand-mark {
    position: absolute; left: 870px; top: 442px; display: flex; align-items: center; gap: 8px;
    color: #d7d7d7; font-weight: 700; font-size: 22px;
  }
  .brand-mark__dot { width: 22px; height: 22px; border-radius: 50%; background: var(--orange); }
  .footer {
    position: absolute; left: 0; top: 506px; width: 1200px; height: 65px;
    background: var(--footer); color: var(--ink);
  }
  .footer__site { position: absolute; left: 307px; top: 13px; font-size: 27px; }
  .footer__rule { position: absolute; top: 12px; width: 1px; height: 40px; background: #8a8a8a; }
  .footer__ring {
    position: absolute; top: 7px; width: 50px; height: 50px; border-radius: 50%;
    border: 2.5px solid var(--ink);
  }
  .footer__handle { position: absolute; top: 19px; font-size: 19px; }
</style>
</head>
<body>
<div class="canvas">
  <div class="backdrop" role="img" aria-label="Warm sunset gradient fading into black with faint binary digits"></div>

  <div class="title-pill">HOW VPN WORKS</div>

  <svg class="diagram-lines" width="1200" height="506" viewBox="0 0 1200 506" aria-hidden="true">
    <g fill="none" stroke="var(--dash)" stroke-width="1" stroke-dasharray="3 3">
      <polyline points="424,196 456,196 456,262 388,262"/>
      <polyline points="678,171 685,171 685,238 662,238"/>
      <polyline points="910,196 946,196 946,262 896,262"/>
      <polyline points="364,324 364,398 880,398 880,324"/>
      <line x1="620" y1="398" x2="620" y2="424"/>
      <line x1="275" y1="324" x2="275" y2="420"/>
    </g>
    <rect x="60" y="284" width="1080" height="40" fill="var(--white)"/>
    <line x1="60" y1="284" x2="1140" y2="284" stroke="var(--orange)" stroke-width="1.5"/>
    <line x1="60" y1="324" x2="1140" y2="324" stroke="var(--orange)" stroke-width="1.5"/>
    <path fill="var(--white)" d="M450,366 C420,366 420,318 452,310 C446,276 480,258 508,270 C516,226 572,212 600,240 C618,204 676,200 700,236 C730,220 770,240 764,278 C790,286 792,328 770,338 C784,356 770,368 750,366 Z"/>
    <g fill="none" stroke="var(--orange)" stroke-width="1.5" stroke-dasharray="4 3">
      <line x1="256" y1="297" x2="286" y2="297"/><line x1="262" y1="311" x2="292" y2="311"/>
      <line x1="410" y1="297" x2="440" y2="297"/><line x1="416" y1="311" x2="446" y2="311"/>
      <line x1="518" y1="297" x2="548" y2="297"/><line x1="524" y1="311" x2="554" y2="311"/>
      <line x1="722" y1="297" x2="752" y2="297"/><line x1="728" y1="311" x2="758" y2="311"/>
      <line x1="920" y1="297" x2="950" y2="297"/><line x1="926" y1="311" x2="956" y2="311"/>
    </g>
    <g fill="var(--orange)">
      <path d="M286,293 l6,4 l-6,4z"/><path d="M262,307 l-6,4 l6,4z"/>
      <path d="M440,293 l6,4 l-6,4z"/><path d="M416,307 l-6,4 l6,4z"/>
      <path d="M548,293 l6,4 l-6,4z"/><path d="M524,307 l-6,4 l6,4z"/>
      <path d="M752,293 l6,4 l-6,4z"/><path d="M728,307 l-6,4 l6,4z"/>
      <path d="M950,293 l6,4 l-6,4z"/><path d="M926,307 l-6,4 l6,4z"/>
      <circle cx="275" cy="425" r="5"/><circle cx="620" cy="432" r="6"/>
    </g>
    <defs>
      <radialGradient id="badgeFill" cx="40%" cy="35%" r="70%">
        <stop offset="0" stop-color="#ffb347"/><stop offset="1" stop-color="var(--orange-deep)"/>
      </radialGradient>
      <g id="lockBadge">
        <circle r="33" fill="url(#badgeFill)" stroke="#ffcf8a" stroke-width="2"/>
        <path d="M0,-20 L16,-14 L16,0 C16,12 8,19 0,22 C-8,19 -16,12 -16,0 L-16,-14 Z" fill="var(--white)"/>
        <path d="M0,-15 L11,-11 L11,0 C11,9 5,14 0,16 C-5,14 -11,9 -11,0 L-11,-11 Z" fill="var(--badge-red)"/>
        <rect x="-6" y="-2" width="12" height="10" rx="1.5" fill="var(--white)"/>
        <path d="M-4,-2 v-3 a4,4 0 0 1 8,0 v3" fill="none" stroke="var(--white)" stroke-width="2"/>
      </g>
    </defs>
    <use href="#lockBadge" x="354" y="304"/>
    <use href="#lockBadge" x="603" y="304"/>
    <use href="#lockBadge" x="870" y="304"/>
  </svg>

  <div class="figure" style="left:320px;top:212px;width:68px;height:62px;" role="img" aria-label="Illustration of a hooded computer hacker trying to look into the tunnel"></div>
  <div class="figure" style="left:840px;top:224px;width:64px;height:50px;" role="img" aria-label="Illustration of a government spy in a hat and sunglasses trying to look into the tunnel"></div>

  <div class="tag" style="left:308px;top:186px;width:116px;">Computer Hacker</div>
  <div class="tag tag--internet" style="left:546px;top:158px;width:132px;">INTERNET</div>
  <div class="tag" style="left:780px;top:186px;width:130px;">Government Spies</div>

  <div class="device" style="left:44px;top:250px;" role="img" aria-label="Laptop showing a video player and a download window"></div>
  <div class="device" style="left:988px;top:250px;" role="img" aria-label="Laptop showing a video player and a download window"></div>

  <div class="device-label" style="left:23px;top:374px;">
    <span class="device-label__title">COMPUTER DEVICE</span>
    <span class="device-label__role">Sender/reciver</span>
  </div>
  <div class="device-label" style="left:981px;top:374px;">
    <span class="device-label__title">COMPUTER DEVICE</span>
    <span class="device-label__role">Sender/reciver</span>
  </div>

  <div class="note" style="left:225px;top:438px;width:100px;">VPN tunnel</div>
  <div class="note" style="left:530px;top:444px;width:200px;">Secure VPN Encryption<br>from outsiders</div>

  <div class="brand-mark"><span class="brand-mark__dot"></span>veilnet.io</div>

  <footer class="footer">
    <div class="footer__site">www.veilnet.io</div>
    <div class="footer__rule" style="left:502px;"></div>
    <div class="footer__ring" style="left:516px;"></div>
    <div class="footer__handle" style="left:578px;">veilnetvpn</div>
    <div class="footer__rule" style="left:692px;"></div>
    <div class="footer__ring" style="left:704px;"></div>
    <div class="footer__handle" style="left:766px;">@veilnetvpn</div>
  </footer>
</div>
</body>
</html>
```